Business Card Design Project

We are looking for an eye catching, unique business card design that incorporates our logo and a photo of the mortgage associate.

We will need to have our business address included (could be on the back of the card), as well as the mortgage associate's information:

Name
Position
Phone
Email

Logo attached.

Target Market(s)

Clients (people purchasing homes, renewing existing mortgages, or refinancing existing mortgages)
Referral sources such as realtors, financial advisors, relocation specialists, real estate lawyers...

Industry/Entity Type

Business

Requirements
Must have
• Logo
Name and contact information of associate
Address of brokerage
Nice to have
• Photo of the agent

```html
<!DOCTYPE html>
<html lang="en">
<head>
<meta charset="utf-8">
<title>Hearth Lane – Business Card</title>
<link rel="stylesheet" href="https://fonts.googleapis.com/css2?family=Jost:wght@400;700&family=Open+Sans:wght@400&family=Crimson+Text:wght@400&display=swap">
<style>
  :root {
    --stage: #dddddd;
    --stage-edge: #d2d2d2;
    --charcoal: #353335;
    --paper: #ffffff;
    --brand-red: #8f1a1e;
    --brand-red-dark: #5e0f12;
    --ink: #262626;
    --rule: #d9d9d9;
    --contact-text: #f2f2f2;
  }
  * { margin: 0; padding: 0; box-sizing: border-box; }
  html, body { width: 1200px; height: 881px; overflow: hidden; }
  body {
    position: relative;
    background: radial-gradient(ellipse at center, #e6e6e6 0%, var(--stage) 60%, var(--stage-edge) 100%);
    font-family: "Open Sans", sans-serif;
  }
  .card {
    position: absolute;
    left: 339px;
    width: 580px;
    height: 348px;
    background: var(--paper);
    overflow: hidden;
    box-shadow: 0 1px 3px rgba(0,0,0,0.12);
  }
  .card--front { top: 59px; overflow: visible; }
  .card--back { top: 486px; }

  /* Front */
  .side-band {
    position: absolute;
    top: 0;
    height: 100%;
    background: var(--charcoal);
  }
  .side-band--left { left: 0; width: 140px; }
  .side-band--right { right: 0; width: 141px; }

  .brand {
    position: absolute;
    left: 140px;
    width: 299px;
    top: 190px;
    display: flex;
    justify-content: center;
    align-items: center;
    gap: 9px;
  }
  .brand-mark {
    flex: none;
    width: 22px;
    height: 22px;
    background: var(--brand-red);
  }
  .brand-name {
    font-family: "Jost", sans-serif;
    font-weight: 700;
    font-size: 27px;
    line-height: 1;
    letter-spacing: 0.3px;
    color: var(--ink);
    white-space: nowrap;
  }

  .ribbon {
    position: absolute;
    display: block;
  }
  .ribbon--tagline { left: 124px; top: 236px; width: 333px; height: 44px; }
  .ribbon-text {
    position: absolute;
    color: #fff;
    white-space: nowrap;
  }
  .tagline {
    left: 124px;
    top: 236px;
    width: 333px;
    height: 33px;
    line-height: 33px;
    text-align: center;
    font-family: "Jost", sans-serif;
    font-size: 13px;
    letter-spacing: 0.6px;
  }

  /* Back */
  .contact-panel {
    position: absolute;
    left: 0; top: 0;
    width: 280px; height: 100%;
    background: var(--charcoal);
  }
  .contact-group {
    position: absolute;
    left: 57px;
    width: 183px;
  }
  .contact-group--address { top: 78px; }
  .contact-group--phone { top: 146px; }
  .contact-group--web { top: 213px; }
  .contact-icon {
    display: block;
    width: 16px;
    height: 16px;
    margin-bottom: 3px;
  }
  .contact-rule {
    height: 1px;
    background: var(--rule);
    margin-bottom: 7px;
  }
  .contact-line {
    font-size: 11.5px;
    line-height: 18px;
    color: var(--contact-text);
    white-space: nowrap;
  }

  .agent-photo {
    position: absolute;
    left: 370px;
    top: 59px;
    width: 111px;
    height: 126px;
    border-radius: 8px;
    background: var(--brand-red);
    border: 1px solid #6e1114;
    box-shadow: 2px 3px 5px rgba(0,0,0,0.35);
    display: flex;
    flex-direction: column;
    justify-content: center;
    align-items: center;
    font-family: "Crimson Text", serif;
    font-size: 19px;
    line-height: 23px;
    letter-spacing: 0.5px;
    color: #f1e4e4;
    text-align: center;
  }
  .ribbon--name { left: 265px; top: 196px; width: 315px; height: 40px; }
  .agent-name {
    left: 265px;
    top: 196px;
    width: 315px;
    height: 32px;
    line-height: 32px;
    text-align: center;
    font-family: "Crimson Text", serif;
    font-size: 20px;
    letter-spacing: 1.5px;
    color: #f4e8e8;
  }
</style>
</head>
<body>

  <section class="card card--front" aria-label="Card front">
    <div class="side-band side-band--left"></div>
    <div class="side-band side-band--right"></div>

    <div class="brand">
      <span class="brand-mark" aria-hidden="true"></span>
      <span class="brand-name">HEARTH LANE</span>
    </div>

    <svg class="ribbon ribbon--tagline" viewBox="0 0 333 44" aria-hidden="true">
      <polygon points="0,33 16,33 16,43" fill="var(--brand-red-dark)"/>
      <polygon points="333,33 317,33 317,43" fill="var(--brand-red-dark)"/>
      <rect x="0" y="0" width="333" height="33" fill="var(--brand-red)"/>
    </svg>
    <p class="ribbon-text tagline">Mortgages for a lifestyle not a life time</p>
  </section>

  <section class="card card--back" aria-label="Card back">
    <div class="contact-panel">
      <div class="contact-group contact-group--address">
        <svg class="contact-icon" viewBox="0 0 16 16" aria-hidden="true">
          <path d="M8 1 L1 7.5 H3 V15 H6.5 V10.5 H9.5 V15 H13 V7.5 H15 Z" fill="#fff"/>
        </svg>
        <div class="contact-rule"></div>
        <p class="contact-line">215 Harbour Street,</p>
        <p class="contact-line">Lakeview 54321</p>
      </div>

      <div class="contact-group contact-group--phone">
        <svg class="contact-icon" viewBox="0 0 16 16" aria-hidden="true">
          <path d="M1 5 Q8 0 15 5 L13 7 L11 5.5 V4.5 Q8 3.5 5 4.5 V5.5 L3 7 Z" fill="#fff"/>
          <path d="M4 8 H12 L14 14 H2 Z" fill="#fff"/>
          <circle cx="8" cy="11" r="1.6" fill="var(--charcoal)"/>
        </svg>
        <div class="contact-rule"></div>
        <p class="contact-line">+000 2468 1357</p>
        <p class="contact-line">+000 2468 1358</p>
      </div>

      <div class="contact-group contact-group--web">
        <svg class="contact-icon" viewBox="0 0 16 16" aria-hidden="true">
          <rect x="1" y="2" width="14" height="9.5" fill="none" stroke="#fff" stroke-width="2"/>
          <rect x="6" y="12" width="4" height="2" fill="#fff"/>
          <rect x="4" y="14" width="8" height="1.5" fill="#fff"/>
        </svg>
        <div class="contact-rule"></div>
        <p class="contact-line">hello@hearthlanehomes.com</p>
        <p class="contact-line">hearthlanehomes.com</p>
      </div>
    </div>

    <div class="agent-photo" role="img" aria-label="Portrait photo of the mortgage associate">
      <span>AGENT</span>
      <span>PICTURE</span>
    </div>

    <svg class="ribbon ribbon--name" viewBox="0 0 315 40" aria-hidden="true">
      <polygon points="0,32 14,32 14,40" fill="var(--brand-red-dark)"/>
      <rect x="0" y="0" width="315" height="32" fill="var(--brand-red)"/>
    </svg>
    <p class="ribbon-text agent-name">YOUR NAME</p>
  </section>

</body>
</html>
```